Business Card Design Project

New Business Card design for Varodine Technology Ltd using new Logo and new Tagline for staffing company.

About us from our website - www.varodine.example:

VaroDine is a leading and recognized Electronic Entertainment, Workforce Augmentation, and Project Management solutions provider with clients in Electronic Entertainment, Legal, Technology, Government and other verticals that range in size from start up organizations to Zenlar 500 companies. VaroDine is certified as an 8(a) minority and woman owned enterprise, established in 1998.

Target Market(s)

Companies in Electronic Entertainment, Legal, Government and Technology

Industry/Entity Type

Business

Requirements
Must have
• Must include in small letters the following information on back:

Established in 1998
8(a)(w)(e), Cage #7KRT9, DUNS #462137580

Front should have the following:
Derek Holloway
Vice President
5820 Birchmont Road
Fallowby, FB 482917
555-318-2746 X 100
555-902-6613 Fax
555-318-2746 Toll Free
name@varodine.example

Our Tagline: Connect • Collaborate • Achieve

```html
<!DOCTYPE html>
<html lang="en">
<head>
<meta charset="utf-8">
<title>VaroDine Business Card</title>
<link rel="stylesheet" href="https://fonts.googleapis.com/css2?family=Lexend:wght@400;800&family=Questrial&display=swap">
<style>
  :root {
    --stage: #d9d9d9;
    --back-bg: #000000;
    --front-bg: #9a9a9a;
    --brand-blue: #0b5fb0;
    --ink-dark: #333333;
    --ink-white: #ffffff;
    --footer-grey: #9a9a9a;
    --frame: #ffffff;
  }
  html, body {
    margin: 0;
    padding: 0;
    overflow: hidden;
  }
  .canvas {
    position: relative;
    width: 1200px;
    height: 901px;
    background: var(--stage);
    overflow: hidden;
  }
  .card {
    position: absolute;
    top: 290px;
    width: 545px;
    height: 389px;
    box-shadow: 0 4px 14px rgba(0,0,0,0.25);
  }
  .card--back { left: 44px; }
  .card--front { left: 624px; }
  .card svg { display: block; width: 100%; height: 100%; }
  .back-bg { fill: var(--back-bg); }
  .front-bg { fill: var(--front-bg); }
  .site-frame { fill: none; stroke: var(--frame); stroke-width: 2.5; }
  .logo-block { fill: var(--back-bg); }
  .logo-name {
    font-family: "Lexend", sans-serif;
    font-weight: 800;
    font-size: 34px;
    fill: var(--ink-white);
  }
  .credentials {
    font-family: "Lexend", sans-serif;
    font-weight: 800;
    font-size: 15px;
    letter-spacing: 0.6px;
    fill: var(--footer-grey);
  }
  .name {
    font-family: "Lexend", sans-serif;
    font-weight: 800;
    font-size: 48px;
    fill: var(--brand-blue);
  }
  .title {
    font-family: "Questrial", sans-serif;
    font-size: 38px;
    fill: var(--brand-blue);
  }
  .contact {
    font-family: "Questrial", sans-serif;
    font-size: 16.5px;
    fill: var(--ink-white);
  }
  .contact .label, .contact .accent { fill: var(--brand-blue); font-weight: 700; }
  .divider { stroke: var(--brand-blue); stroke-width: 3; }
  .tagline {
    font-family: "Lexend", sans-serif;
    font-weight: 800;
    font-size: 27px;
    letter-spacing: 0.8px;
    fill: var(--ink-dark);
  }
</style>
</head>
<body>
<div class="canvas">

  <section class="card card--back" aria-label="Card back">
    <svg viewBox="0 0 645 461" xmlns="http://www.w3.org/2000/svg">
      <defs>
        <linearGradient id="site-tone" x1="0" y1="0" x2="1" y2="1">
          <stop offset="0" stop-color="#3a3a3e"/>
          <stop offset="0.35" stop-color="#7d6f9e"/>
          <stop offset="0.55" stop-color="#c9bfd8"/>
          <stop offset="1" stop-color="#e8e8e8"/>
        </linearGradient>
      </defs>
      <rect class="back-bg" width="645" height="461"/>
      <rect x="12" y="13" width="621" height="415" fill="url(#site-tone)"
            role="img" aria-label="Screenshot of the VaroDine website with navigation, banner photo of people jumping at sunset, and About Us text"/>
      <rect class="logo-block" x="468" y="318" width="170" height="105"/>
      <text class="logo-name" x="553" y="392" text-anchor="middle">VaroDine</text>

      <g class="site-grid">
        <rect class="site-frame" x="12" y="13" width="128" height="60" rx="8"/>
        <rect class="site-frame" x="146" y="13" width="487" height="128" rx="8"/>
        <rect class="site-frame" x="12" y="78" width="128" height="345" rx="8"/>
        <rect class="site-frame" x="146" y="146" width="128" height="277" rx="8"/>
        <rect class="site-frame" x="278" y="146" width="218" height="127" rx="8"/>
        <rect class="site-frame" x="502" y="146" width="131" height="127" rx="8"/>
        <rect class="site-frame" x="278" y="278" width="187" height="145" rx="8"/>
        <rect class="site-frame" x="469" y="278" width="164" height="38" rx="6"/>
      </g>

      <text class="credentials" x="13" y="447">Established in 1998 8(a)(w)(e), Cage #7KRT9, DUNS #462137580</text>
    </svg>
  </section>

  <section class="card card--front" aria-label="Card front">
    <svg viewBox="0 0 645 460" xmlns="http://www.w3.org/2000/svg">
      <rect class="front-bg" width="645" height="460"/>
      <text class="name" x="323" y="232" text-anchor="middle">Derek Holloway</text>
      <text class="title" x="325" y="267" text-anchor="middle">Vice President</text>

      <g class="contact">
        <text x="19" y="346">5820 Birchmont Road</text>
        <text x="19" y="366">Fallowby, FB 482917</text>
      </g>
      <line class="divider" x1="209" y1="332" x2="209" y2="386"/>
      <g class="contact" text-anchor="middle">
        <text x="323" y="346"><tspan class="label">t</tspan> 555-318-2746 X 100</text>
        <text x="323" y="366"><tspan class="label">f</tspan> 555-902-6613</text>
        <text x="323" y="386">555-318-2746 <tspan class="accent">Toll Free</tspan></text>
      </g>
      <line class="divider" x1="433" y1="332" x2="433" y2="386"/>
      <g class="contact" text-anchor="end">
        <text x="628" y="346"><tspan class="label">e</tspan> name@varodine.example</text>
        <text x="628" y="366"><tspan class="label">w</tspan> www.varodine.example</text>
      </g>

      <text class="tagline" x="323" y="428" text-anchor="middle">Connect • Collaborate • Achieve</text>
    </svg>
  </section>

</div>
</body>
</html>
```